Brochure design for trade company

I would like to get a professional, easy to read and eye catchy capability statement designed for my electrical business.

My aim is to be able to go to property managers and WOW them when they see the capability statement.

Attached the content writing, design brief, company logo and template of what I like below. If there are any questions please send me a message.

The areas we service photo is an example, please do your own designs for the maps section

Thank you in advance for the help team.

Requirements
Must have
• The areas we service photo is an example, please do your own designs for the maps section
Nice to have
• Eye catching and creative. Also be warm & inviting
Should not have
• Not too out of place looking photos or elements. Don’t make it he design look too cold

```html
<!DOCTYPE html>
<html lang="en">
<head>
<meta charset="utf-8">
<title>Brightwire Electrical – Capability Statement</title>
<link href="https://fonts.googleapis.com/css2?family=Krona+One&family=Oswald:wght@600&family=Poppins:wght@400;500;600&display=swap" rel="stylesheet">
<style>
:root{
  --ink:#141414;
  --panel:#222222;
  --panel-light:#3a3a3a;
  --orange:#f0a03a;
  --white:#ffffff;
  --grey:#d6d6d6;
  --line:#bfbfbf;
}
*{margin:0;padding:0;box-sizing:border-box}
html,body{width:1200px;height:4983px;overflow:hidden;background:var(--white)}
body{position:relative;font-family:"Poppins",sans-serif;color:var(--white)}
.page{position:absolute;left:37px;width:1132px;height:1602px;overflow:hidden;
  background:linear-gradient(180deg,var(--ink) 0%,var(--panel) 55%,var(--panel-light) 100%)}
.page-cover{top:35px;background:var(--ink)}
.page-about{top:1687px}
.page-services{top:3346px}
.abs{position:absolute}
.heading{font-family:"Krona One",sans-serif;text-transform:uppercase;color:var(--white);letter-spacing:1px}
.accent{color:var(--orange)}
.brand{font-family:"Poppins",sans-serif;font-weight:600;color:var(--white);text-transform:uppercase;text-align:center;line-height:1}
.brand .brand-main{display:block;letter-spacing:4px}
.brand .brand-sub{display:block;letter-spacing:10px}
.corner-tab{position:absolute;left:0;top:58px;width:64px;height:62px;background:var(--orange)}
.footer{position:absolute;left:0;right:0;top:1538px;display:flex;justify-content:center;gap:22px;font-size:21px;align-items:center}
.footer span{display:flex;align-items:center;gap:8px}
.footer svg{width:22px;height:22px;fill:var(--orange)}
/* cover */
.cover-photo{left:0;top:340px;width:1132px;height:1110px;
  background:linear-gradient(160deg,#0d0d0d 0%,#5a5a5a 45%,#2a2a2a 70%,#111 100%)}
.sector-band{left:0;top:1448px;width:1132px;height:62px;background:var(--orange);color:var(--ink);
  font-size:24px;letter-spacing:5px;display:flex;align-items:center;justify-content:center;font-weight:500}
/* about */
.section-label{font-size:30px;letter-spacing:6px;color:var(--orange);font-weight:500}
.intro{left:90px;width:960px;font-size:20px;line-height:25px;text-align:justify}
.rule{left:90px;width:960px;height:2px;background:var(--line)}
.value-card{position:absolute;top:766px;width:218px;height:189px;border:4px solid var(--orange);border-top:none}
.value-card::before,.value-card::after{content:"";position:absolute;top:0;height:4px;width:38px;background:var(--orange)}
.value-card::before{left:0}.value-card::after{right:0}
.value-icon{position:absolute;top:-50px;left:50%;transform:translateX(-50%);width:80px;height:80px;background:var(--panel);display:flex;justify-content:center;align-items:center}
.value-icon svg{width:64px;height:64px;stroke:var(--white);fill:none;stroke-width:3}
.value-name{position:absolute;top:34px;left:0;right:0;text-align:center;font-family:"Oswald",sans-serif;font-size:25px;line-height:36px;color:var(--white)}
.value-bolt{position:absolute;bottom:-44px;left:50%;transform:translateX(-50%);width:40px;height:64px;background:var(--panel)}
.promise{position:absolute;width:470px;display:flex;gap:22px;font-size:20px;line-height:25px}
.promise-num{flex:0 0 62px;height:64px;border:4px solid var(--orange);font-family:"Krona One",sans-serif;font-size:40px;display:flex;align-items:center;justify-content:center}
/* services */
.service{position:absolute;display:flex;align-items:center;gap:18px;font-size:21px;line-height:25px;width:520px}
.service svg{flex:0 0 44px;height:44px;stroke:var(--orange);fill:none;stroke-width:2.5}
.review-badge{left:98px;top:1087px;width:377px;height:110px;border-radius:55px;background:#3f5fbf;opacity:.9}
.stars{left:150px;top:1205px;display:flex;gap:8px}
.stars svg{width:46px;height:46px;fill:#f4b400}
.map-area{left:578px;top:878px;width:458px;height:446px;border:7px solid var(--orange);border-radius:22px;
  background:linear-gradient(135deg,#e9ece8 0%,#dfe6e1 55%,#b9d3e8 100%)}
.credential{left:620px;font-size:15px;letter-spacing:4px;color:var(--orange)}
</style>
</head>
<body>

<!-- Cover -->
<section class="page page-cover">
  <div class="brand abs" style="left:0;right:0;top:70px">
    <span class="brand-main" style="font-size:78px">Brightwire</span>
    <span class="brand-sub" style="font-size:38px;margin-top:10px">Electrical</span>
  </div>
  <h1 class="heading abs" style="left:0;right:0;top:272px;text-align:center;font-size:36px">Capability Statement</h1>
  <p class="abs accent" style="left:0;right:0;top:314px;text-align:center;font-size:22px;letter-spacing:5px">WHEN QUALITY AND RELIABILITY COUNTS</p>
  <div class="cover-photo abs" role="img" aria-label="Black and white upward view of a modern brick apartment tower with glass balconies"></div>
  <div class="sector-band abs">RESIDENTIAL | COMMERCIAL | REAL ESTATE | STRATA</div>
  <div class="footer">
    <span><svg viewBox="0 0 24 24"><path d="M2 5h20v14H2z M2 5l10 8 10-8" /></svg>hello@brightwireelectrical.com.au</span>
    <span><svg viewBox="0 0 24 24"><circle cx="12" cy="12" r="10"/></svg>brightwireelectrical.com.au</span>
    <span><svg viewBox="0 0 24 24"><path d="M6 2l4 5-2 3c1 3 3 5 6 6l3-2 5 4-3 4C10 22 2 14 2 5z"/></svg>0400 123 987</span>
  </div>
</section>

<!-- About -->
<section class="page page-about">
  <div class="corner-tab"></div>
  <h2 class="heading abs" style="left:90px;top:60px;font-size:46px">About Us</h2>
  <div class="brand abs" style="left:762px;top:66px;width:275px">
    <span class="brand-main" style="font-size:32px">Brightwire</span>
    <span class="brand-sub" style="font-size:15px;margin-top:4px">Electrical</span>
  </div>
  <h3 class="section-label abs" style="left:90px;top:180px">WHO WE ARE</h3>
  <p class="intro abs" style="top:256px">Brightwire Electrical, we’re more than just a team of electricians—we’re your extended family that you can rely on 24/7 for reliable, expert help for anything electrical related.</p>
  <p class="intro abs" style="top:330px">With our friendly, reliable, and no-nonsense approach, we ensure that your needs are met with professionalism and a smile. Whether it’s a small repair or a major installation, we’re here to make your life easier.</p>
  <div class="rule abs" style="top:460px"></div>
  <p class="abs accent" style="left:90px;top:484px;font-size:24px;letter-spacing:3px">AT BRIGHTWIRE ELECTRICAL, WE MAKE SURE THAT EVERY JOB COUNTS.</p>
  <div class="rule abs" style="top:538px"></div>
  <h2 class="heading abs" style="left:0;right:0;top:612px;text-align:center;font-size:48px"><span class="accent">Core</span> Values</h2>

  <div class="value-card" style="left:92px">
    <div class="value-icon"><svg viewBox="0 0 64 64"><path d="M32 6l22 8v16c0 14-10 24-22 28C20 54 10 44 10 30V14z"/><path d="M22 32l8 8 14-16"/></svg></div>
    <div class="value-name">Reliability<br>and<br>safety first</div>
    <svg class="value-bolt" viewBox="0 0 40 64"><path d="M26 2L8 36h12L14 62 32 26H20z" fill="#f0a03a"/></svg>
  </div>
  <div class="value-card" style="left:334px">
    <div class="value-icon"><svg viewBox="0 0 64 64"><path d="M4 26l12-10 10 4 8-4 10 2 16 8"/><path d="M16 36l10 10 4-4 4 4 4-4 4 2 8-10"/></svg></div>
    <div class="value-name">Community<br>and<br>respect</div>
    <svg class="value-bolt" viewBox="0 0 40 64"><path d="M26 2L8 36h12L14 62 32 26H20z" fill="#f0a03a"/></svg>
  </div>
  <div class="value-card" style="left:576px">
    <div class="value-icon"><svg viewBox="0 0 64 64"><circle cx="30" cy="34" r="22"/><circle cx="30" cy="34" r="12"/><path d="M30 34L54 10M48 8h8v8"/></svg></div>
    <div class="value-name" style="top:52px">Customer<br>Focused</div>
    <svg class="value-bolt" viewBox="0 0 40 64"><path d="M26 2L8 36h12L14 62 32 26H20z" fill="#f0a03a"/></svg>
  </div>
  <div class="value-card" style="left:818px">
    <div class="value-icon"><svg viewBox="0 0 64 64"><path d="M6 30h10v26H6zM16 32l10-14V8c6 0 8 6 6 14h14c4 0 4 6 0 6 4 0 4 6 0 6 4 0 4 6 0 6 3 0 3 6-1 6H16"/><circle cx="50" cy="14" r="10"/><path d="M45 14l4 4 6-7"/></svg></div>
    <div class="value-name">Openness,<br>trust and<br>accountability</div>
    <svg class="value-bolt" viewBox="0 0 40 64"><path d="M26 2L8 36h12L14 62 32 26H20z" fill="#f0a03a"/></svg>
  </div>

  <h3 class="section-label abs" style="left:94px;top:1064px;font-size:32px">OUR PROMISE TO YOU</h3>
  <div class="rule abs" style="left:596px;width:438px;top:1085px"></div>

  <div class="promise" style="left:90px;top:1188px"><div class="promise-num">1</div><p>Around clock communication.<br>We can always be reached 24/7</p></div>
  <div class="promise" style="left:563px;top:1188px"><div class="promise-num">2</div><p>Reliability and speed, quotations<br>and WO’s actioned promptly</p></div>
  <div class="promise" style="left:90px;top:1340px"><div class="promise-num" style="margin-top:8px">3</div><p>Service with a smile on our face. We take the stress out of daily life and let you do the things you want to do</p></div>
  <div class="promise" style="left:563px;top:1340px"><div class="promise-num" style="margin-top:8px">4</div><p>All our staff are trained to the highest level with expert knowledge in the industry to make a tailored solution for clients</p></div>

  <div class="footer">
    <span><svg viewBox="0 0 24 24"><path d="M2 5h20v14H2z"/></svg>hello@brightwireelectrical.com.au</span>
    <span><svg viewBox="0 0 24 24"><circle cx="12" cy="12" r="10"/></svg>brightwireelectrical.com.au</span>
    <span><svg viewBox="0 0 24 24"><path d="M6 2l4 5-2 3c1 3 3 5 6 6l3-2 5 4-3 4C10 22 2 14 2 5z"/></svg>0400 123 987</span>
  </div>
</section>

<!-- Services -->
<section class="page page-services">
  <div class="corner-tab"></div>
  <h2 class="heading abs" style="left:90px;top:52px;font-size:46px;line-height:61px">Our<br>Maintenance<br>Services</h2>
  <div class="brand abs" style="left:762px;top:66px;width:275px">
    <span class="brand-main" style="font-size:32px">Brightwire</span>
    <span class="brand-sub" style="font-size:15px;margin-top:4px">Electrical</span>
  </div>

  <div class="service" style="left:100px;top:301px"><svg viewBox="0 0 44 44"><circle cx="22" cy="22" r="18"/><path d="M22 12v10l7 5"/></svg>24/7 Emergency services</div>
  <div class="service" style="left:100px;top:376px"><svg viewBox="0 0 44 44"><circle cx="22" cy="14" r="10"/><path d="M22 24v18"/></svg>Fault finding and diagnostics</div>
  <div class="service" style="left:100px;top:454px"><svg viewBox="0 0 44 44"><rect x="4" y="10" width="36" height="24"/><path d="M12 16v12M20 16v12M28 16v12"/></svg>Switchboard upgrade &amp; repairs</div>
  <div class="service" style="left:100px;top:531px"><svg viewBox="0 0 44 44"><rect x="4" y="6" width="36" height="32"/><path d="M24 10L14 24h8l-4 12 12-16h-8z"/></svg>General lighting installations<br>&amp; repairs</div>
  <div class="service" style="left:100px;top:630px"><svg viewBox="0 0 44 44"><circle cx="22" cy="22" r="18"/><path d="M25 8L14 24h8l-3 12 11-16h-8z"/></svg>PowerPoint installation</div>
  <div class="service" style="left:100px;top:715px"><svg viewBox="0 0 44 44"><rect x="12" y="4" width="20" height="36"/><circle cx="22" cy="28" r="4"/><path d="M22 12v12"/></svg>Electric storage hot water<br>systems service</div>

  <div class="service" style="left:560px;top:301px"><svg viewBox="0 0 44 44"><path d="M8 4h28M12 10h20"/><path d="M22 16c6 6 8 10 8 14a8 8 0 0 1-16 0c0-4 2-8 8-14z"/></svg>Smoke alarm installation &amp; compliance</div>
  <div class="service" style="left:560px;top:376px"><svg viewBox="0 0 44 44"><circle cx="22" cy="22" r="12"/><circle cx="22" cy="22" r="5"/><path d="M22 4v6M22 34v6M4 22h6M34 22h6"/></svg>Appliance repair/ installations</div>
  <div class="service" style="left:560px;top:454px"><svg viewBox="0 0 44 44"><circle cx="22" cy="14" r="8"/><circle cx="12" cy="28" r="8"/><circle cx="32" cy="28" r="8"/></svg>Ventiatlion&amp;mould prevention – ceiling<br>fans, exhaust fans, underfloor ventilation</div>
  <div class="service" style="left:560px;top:541px"><svg viewBox="0 0 44 44"><rect x="4" y="8" width="36" height="24"/><path d="M16 38h12"/><circle cx="22" cy="20" r="5"/></svg>TV,Data and antenna services</div>
  <div class="service" style="left:560px;top:630px"><svg viewBox="0 0 44 44"><path d="M22 4l16 6v12c0 10-8 16-16 18C14 38 6 32 6 22V10z"/><path d="M25 12l-8 12h7l-3 8 8-12h-7z"/></svg>Surge protection</div>
  <div class="service" style="left:560px;top:715px"><svg viewBox="0 0 44 44"><rect x="18" y="6" width="20" height="32"/><path d="M6 14v10a4 4 0 0 0 8 0v-6h4"/><path d="M28 14l-4 8h6l-4 8"/></svg>EV charging systems and lighting<br>upgrades for commercial premises</div>

  <h2 class="heading abs" style="left:96px;top:900px;font-size:46px;line-height:61px">Areas We<br>Service</h2>
  <div class="review-badge abs" role="img" aria-label="Five-star customer review badge"></div>
  <div class="stars abs">
    <svg viewBox="0 0 24 24"><path d="M12 2l3 7 7 .5-5.5 4.5 2 7L12 17l-6.5 4 2-7L2 9.5 9 9z"/></svg>
    <svg viewBox="0 0 24 24"><path d="M12 2l3 7 7 .5-5.5 4.5 2 7L12 17l-6.5 4 2-7L2 9.5 9 9z"/></svg>
    <svg viewBox="0 0 24 24"><path d="M12 2l3 7 7 .5-5.5 4.5 2 7L12 17l-6.5 4 2-7L2 9.5 9 9z"/></svg>
    <svg viewBox="0 0 24 24"><path d="M12 2l3 7 7 .5-5.5 4.5 2 7L12 17l-6.5 4 2-7L2 9.5 9 9z"/></svg>
    <svg viewBox="0 0 24 24"><path d="M12 2l3 7 7 .5-5.5 4.5 2 7L12 17l-6.5 4 2-7L2 9.5 9 9z"/></svg>
  </div>
  <div class="map-area abs" role="img" aria-label="Map of the Sydney metropolitan service area"></div>

  <p class="abs" style="left:96px;top:1336px;font-size:26px;letter-spacing:6px">CONTACT</p>
  <p class="abs accent" style="left:94px;top:1366px;font-size:58px;letter-spacing:10px;font-weight:600">DANIEL REYES</p>
  <p class="abs" style="left:96px;top:1444px;font-size:24px;letter-spacing:4px"><span class="accent">DIRECTOR</span> 0400 123 987</p>
  <div class="rule abs" style="left:575px;width:466px;top:1392px;height:1px"></div>
  <p class="credential abs" style="top:1412px">ELECTRICAL SUPERVISORS LICENCE : 100234X</p>
  <p class="credential abs" style="top:1431px">COMPANY ABN : 12 345 678 901</p>
  <div class="rule abs" style="left:575px;width:466px;top:1474px;height:1px"></div>

  <div class="footer">
    <span><svg viewBox="0 0 24 24"><path d="M2 5h20v14H2z"/></svg>hello@brightwireelectrical.com.au</span>
    <span><svg viewBox="0 0 24 24"><circle cx="12" cy="12" r="10"/></svg>brightwireelectrical.com.au</span>
    <span><svg viewBox="0 0 24 24"><path d="M6 2l4 5-2 3c1 3 3 5 6 6l3-2 5 4-3 4C10 22 2 14 2 5z"/></svg>0400 123 987</span>
  </div>
</section>

</body>
</html>
```